A starter web site for the Brisco Tandem Works Association. Our target market are companies that use cyber security products and services and those who provide them.

Target Market(s)

Companies that provide cyber security products and services.

Industry/Entity Type

Security

Coding

Coded - Design and coding required

Number of Pages Required

5+ page

Font styles to use
Serif

Requirements
Must have
• We need the site to have an editor so we can add content, pictures and links to video on Flicora.
Nice to have
• If possible a way to collect names of people interested in joining the organization. that falls into a excel spreadsheet.
Should not have
• Hard to read characters

```html
<!DOCTYPE html>
<html lang="en">
<head>
<meta charset="utf-8">
<title>Brisco Tandem Works Association</title>
<link href="https://fonts.googleapis.com/css2?family=Arimo:wght@400;700&family=Michroma&family=Roboto+Condensed:wght@300;400&display=swap" rel="stylesheet">
<style>
:root{
  --red:#ee2d2d;
  --ink:#555555;
  --ink-soft:#777777;
  --ink-dark:#333333;
  --rule:#e3e3e3;
  --page:#ffffff;
  --band:#f0eff0;
  --footer:#444444;
  --dark-band:#2e2e2e;
  --white:#ffffff;
}
*{margin:0;padding:0;box-sizing:border-box}
html,body{width:956px;height:1200px;overflow:hidden;background:var(--page)}
body{font-family:"Arimo",Arial,sans-serif;color:var(--ink);font-size:8px}
.wrap{width:560px;margin:0 auto}
.display{font-family:"Michroma",sans-serif;text-transform:uppercase;letter-spacing:2px}

/* header */
.site-header{height:86px}
.main-nav{height:23px;border-bottom:1px solid var(--rule);display:flex;justify-content:center;align-items:center}
.main-nav a{color:var(--ink-soft);text-decoration:none;font-size:7.5px;padding:0 20px}
.brand{text-align:center;margin-top:15px;font-size:12px;color:#444;letter-spacing:2.5px}
.social{display:flex;justify-content:center;gap:4px;margin-top:7px}
.social span{display:inline-block;border:1px solid #cfcfcf;border-radius:2px;padding:2px 5px;font-size:7px;color:#555;background:#fafafa}

/* hero */
.hero{position:relative;height:280px;overflow:hidden;background:radial-gradient(ellipse at 78% 30%,#1d3556 0%,#0b1522 35%,#05080c 70%),#05080c}
.hero-art{position:absolute;inset:0}
.hero-tagline{position:absolute;left:411px;top:186px;font-family:"Roboto Condensed",sans-serif;color:var(--white);line-height:1;white-space:nowrap}
.hero-tagline .small{display:block;font-size:12px;letter-spacing:3.5px;font-weight:300;color:#d8d8d8}
.hero-tagline .line{display:flex;align-items:flex-end}
.hero-tagline .big{font-size:22px;font-weight:400;color:var(--white);margin-right:2px}
.hero-tagline .pct{font-size:34px;color:var(--red);margin-bottom:-3px}

/* welcome */
.welcome{height:180px;text-align:center;padding-top:31px}
.section-title{font-size:12px;color:#444;font-weight:400}
.section-sub{font-size:7px;color:var(--ink-soft);margin-top:8px}
.welcome .wrap{width:600px}
.goals{display:flex;justify-content:space-between;margin-top:20px;padding:0 8px}
.goal{width:124px;font-size:6.6px;line-height:1.45;color:#555}
.goal-icon{width:24px;height:24px;background:var(--red);margin:0 auto 8px;display:flex;align-items:center;justify-content:center}

/* membership */
.membership{height:240px;background:var(--band);text-align:center;padding-top:26px}
.member-box{width:466px;height:119px;margin:10px auto 0;background:#fff;display:flex;text-align:left}
.benefits{width:233px;border-right:1px solid #eee;padding:17px 0 0 14px;list-style:none}
.benefits li{font-size:6.6px;font-weight:700;color:#555;display:flex;gap:8px;margin-bottom:8px;line-height:1.45}
.benefits svg{flex:none;margin-top:1px}
.pricing{padding:17px 0 0 20px;list-style:none}
.pricing li{font-size:6.6px;color:#555;margin-bottom:4.7px}
.pricing li::before{content:"•";margin-right:8px;color:#777}
.btn{display:inline-block;margin-top:18px;width:87px;height:24px;line-height:24px;background:var(--red);color:#fff;font-size:7px;font-weight:700;text-decoration:none}

/* programs */
.programs{position:relative;height:138px;text-align:center;color:#fff}
.programs-bg{position:absolute;inset:0;background:radial-gradient(ellipse at 55% 80%,#5a2020 0%,#3a3a3a 40%,#262626 100%)}
.programs-inner{position:relative;padding-top:28px}
.programs h2{font-size:11px;font-weight:400}
.programs p{width:440px;margin:12px auto 0;font-size:7px;line-height:1.45;color:#eee}
.programs a{display:inline-block;margin-top:11px;color:#fff;font-size:8.5px;font-weight:700}

/* feeds */
.feeds{height:166px;display:flex;gap:20px;width:560px;margin:0 auto;padding-top:24px}
.feed{width:174px}
.feed h3{font-family:"Michroma",sans-serif;font-size:7.5px;font-weight:400;letter-spacing:1.5px;color:#444;padding-bottom:8px;border-bottom:1px solid var(--rule);text-transform:uppercase}
.event{display:flex;gap:10px;margin-top:14px}
.date{flex:none;width:38px;height:36px;background:var(--red);color:#fff;text-align:center;padding-top:6px}
.date b{display:block;font-size:11px}
.date span{font-size:6px}
.event h4{font-size:7px;color:#333}
.event p{font-size:6.5px;line-height:1.4;margin-top:4px}
.media-item{display:flex;gap:8px;margin-top:14px}
.media-item svg{flex:none}
.media-item p{font-size:6.6px;color:#666}
.media-item small{display:block;font-size:5.5px;color:#999;margin-top:4px}
.thumbs{display:flex;gap:6px;margin-top:11px}
.thumb{width:84px;height:56px}
.thumb.clock{background:linear-gradient(135deg,#cfd9e0,#8fa2b0)}
.thumb.crowd{background:linear-gradient(135deg,#9fc8e6,#d59a4a 70%,#6a8a3a)}

/* footer */
.site-footer{height:110px;background:var(--footer);text-align:center;color:#fff;padding-top:41px}
.site-footer .brand-foot{font-size:8.5px;letter-spacing:2px}
.site-footer hr{width:236px;margin:8px auto 0;border:0;border-top:1px solid #777}
.site-footer small{display:block;font-size:6px;color:#ccc;margin-top:9px}
</style>
</head>
<body>

<header class="site-header">
  <nav class="main-nav wrap">
    <a href="#">Home</a><a href="#">Leadership</a><a href="#">Membership</a><a href="#">Cyber</a><a href="#">Media</a><a href="#">Industry Information</a><a href="#">BTWA Contact</a>
  </nav>
  <div class="brand display">Brisco Tandem Works Association</div>
  <div class="social"><span>Chirpline</span><span>Friendhall</span><span>Gadabout</span></div>
</header>

<section class="hero">
  <div class="hero-art" role="img" aria-label="Dark blue abstract metallic panels with glowing light"></div>
  <div class="hero-tagline">
    <span class="small">INFORMATION</span>
    <span class="line"><span class="big">PROTECTED</span><span class="pct">100%</span></span>
  </div>
</section>

<section class="welcome">
  <div class="wrap">
    <h1 class="section-title display">Welcome!</h1>
    <p class="section-sub">Lorem ipsum dolor sit amet, consectetur adipiscing elit. Nulla blandit enim ut leo porta porta</p>
    <div class="goals">
      <div class="goal">
        <div class="goal-icon"><svg width="14" height="14" viewBox="0 0 14 14" fill="none" stroke="#fff" stroke-width="1.5"><path d="M2 2l10 10M12 2L2 12"/></svg></div>
        To encourage cyber security professionals to share best practices, obtain knowledge about new products/services and to constantly improve the protection of businesses located in the Commonwealth.
      </div>
      <div class="goal">
        <div class="goal-icon"><svg width="14" height="14" viewBox="0 0 14 14" fill="none" stroke="#fff" stroke-width="1.3"><circle cx="7" cy="7" r="5.5"/><path d="M7 4v3l2 1"/></svg></div>
        To educate small business owners and the public at large about cyber security to defend companies against cyber theft of data and funds.
      </div>
      <div class="goal">
        <div class="goal-icon"><svg width="14" height="14" viewBox="0 0 14 14" fill="none" stroke="#fff" stroke-width="1.3"><circle cx="5" cy="8" r="3"/><circle cx="10" cy="5" r="2.2"/></svg></div>
        To be the media face for educating the public on cyber threats and defenses against hackers/cyber thieves.
      </div>
      <div class="goal">
        <div class="goal-icon"><svg width="14" height="14" viewBox="0 0 14 14" fill="#fff"><rect x="3" y="6" width="8" height="6"/><path d="M4.5 6V4.5a2.5 2.5 0 015 0V6" fill="none" stroke="#fff" stroke-width="1.3"/></svg></div>
        To education public servants about cyber security issues
      </div>
    </div>
  </div>
</section>

<section class="membership">
  <h2 class="section-title display">About BTWA Membership</h2>
  <p class="section-sub">Members will receive the following benefits</p>
  <div class="member-box">
    <ul class="benefits">
      <li><svg width="7" height="6" viewBox="0 0 7 6"><path d="M.5 3l2 2L6.5.8" fill="none" stroke="#ee2d2d" stroke-width="1.5"/></svg>Product discounts</li>
      <li><svg width="7" height="6" viewBox="0 0 7 6"><path d="M.5 3l2 2L6.5.8" fill="none" stroke="#ee2d2d" stroke-width="1.5"/></svg>Research and surveys on cyber security issues</li>
      <li><svg width="7" height="6" viewBox="0 0 7 6"><path d="M.5 3l2 2L6.5.8" fill="none" stroke="#ee2d2d" stroke-width="1.5"/></svg>Private label newsletter to be sent to clients and employees</li>
      <li><svg width="7" height="6" viewBox="0 0 7 6"><path d="M.5 3l2 2L6.5.8" fill="none" stroke="#ee2d2d" stroke-width="1.5"/></svg>Private label cyber security alerts that can be sent to their clients and employees</li>
      <li><svg width="7" height="6" viewBox="0 0 7 6"><path d="M.5 3l2 2L6.5.8" fill="none" stroke="#ee2d2d" stroke-width="1.5"/></svg>Monthly conference call roundtables</li>
    </ul>
    <ul class="pricing">
      <li>1 to 3 employees- $250 a year</li>
      <li>5 to10 employees- $500 a year</li>
      <li>11 to 20 employees- $1,000 a year</li>
      <li>30 to 50 employees- $2,000 a year</li>
      <li>51 to 75 employees- $3,000 a year</li>
      <li>76 to 100 employees- $4,000 a year</li>
      <li>101 and up employees- $5,000 a year</li>
    </ul>
  </div>
  <a class="btn" href="#">MEMBERSHIP NOW</a>
</section>

<section class="programs">
  <div class="programs-bg" role="img" aria-label="Close-up of a keyboard with a red key"></div>
  <div class="programs-inner">
    <h2 class="display">Online and classroom educational programs</h2>
    <p>Cyber theft of data is growing every year. The Brisco Tandem Works Association mission is to provide information and educate members and their clients on cyber threats and ways to defend business computer systems from hackers. The cost of membership depends on the size of the organization ranging from individuals $149 to $5,000 for large corporate members.</p>
    <a href="#">Link to Ticket Vault</a>
  </div>
</section>

<section class="feeds">
  <div class="feed">
    <h3>Events</h3>
    <div class="event"><div class="date"><b>06</b><span>NOV</span></div><div><h4>Lorem Ipsum is simply dummy</h4><p>Lorem Ipsum is simply dummy text of the printing and typesetting industry. Lorem Ipsum has been the industry</p></div></div>
    <div class="event"><div class="date"><b>06</b><span>NOV</span></div><div><h4>Lorem Ipsum is simply dummy</h4><p>Lorem Ipsum is simply dummy text of the printing and typesetting industry. Lorem Ipsum has been the industry</p></div></div>
  </div>
  <div class="feed">
    <h3>Media</h3>
    <div class="media-item"><svg width="8" height="8" viewBox="0 0 8 8"><rect width="8" height="8" fill="#ee2d2d"/><path d="M1.8 4l1.5 1.5L6.3 2.5" fill="none" stroke="#fff" stroke-width="1.2"/></svg><p>Lorem Ipsum is simply dummy text of the printing<small>12 Dec 2014 &nbsp;|&nbsp; 4 Comments</small></p></div>
    <div class="media-item"><svg width="8" height="8" viewBox="0 0 8 8"><rect width="8" height="8" fill="#ee2d2d"/><path d="M1.8 4l1.5 1.5L6.3 2.5" fill="none" stroke="#fff" stroke-width="1.2"/></svg><p>Lorem Ipsum is simply dummy text of the printing<small>12 Dec 2014 &nbsp;|&nbsp; 4 Comments</small></p></div>
    <div class="media-item"><svg width="8" height="8" viewBox="0 0 8 8"><rect width="8" height="8" fill="#ee2d2d"/><path d="M1.8 4l1.5 1.5L6.3 2.5" fill="none" stroke="#fff" stroke-width="1.2"/></svg><p>Lorem Ipsum is simply dummy text of the printing<small>12 Dec 2014 &nbsp;|&nbsp; 4 Comments</small></p></div>
  </div>
  <div class="feed">
    <h3>Research Center</h3>
    <div class="thumbs">
      <div class="thumb clock" role="img" aria-label="Photo of a clock face"></div>
      <div class="thumb crowd" role="img" aria-label="Photo of a cheering group outdoors"></div>
    </div>
  </div>
</section>

<footer class="site-footer">
  <div class="brand-foot display">Brisco Tandem Works Association</div>
  <hr>
  <small>Copyright © 2014 Company Name Here. All rights reserved.</small>
</footer>

</body>
</html>
```